Corvella Paintless Dent Removal

Our company works on vehicles removing dents using a highly skilled trade which the metal is massaged out with special tools without disturbing the original paint, hence paintless dent removal. Besides keeping the paint and metal original its also very environmentally friendly since no paint or toxic fillers are used. Also we we are one of the most experienced companies in the business with 25 years

Target Market(s)

Retail Automobile consumers, Auto Dealerships and Auto Body Shops

Industry/Entity Type

Auto Repair

Contact Information for Business Card

Dennis Holbrook
PO Box 538 Ashmere, NY 11952
631-472-8816
corvellapdr@mailnest.example
website corvellapdr.example
youtube corvella paintless dent removal
25 years of experience removing Dents, Dings and Hail Damage

Font styles to use
Serif
Sans Serif

Colors

Designer to choose colors to be used in the design.

Requirements
Must have
• I do like things that are simple but classy and somewhat bold, also I like my logo so that should be somewhat important

```html
<!DOCTYPE html>
<html lang="en">
<head>
<meta charset="utf-8">
<title>Corvella Paintless Dent Removal – Business Card</title>
<link rel="stylesheet" href="https://fonts.googleapis.com/css2?family=Open+Sans:wght@400;700;800&display=swap">
<style>
  :root {
    --navy: #13234a;
    --green: #5cb845;
    --white: #ffffff;
    --paper: #f3f3f1;
    --backdrop: #dcdcd8;
    --body-font: "Open Sans", Arial, sans-serif;
  }
  * { margin: 0; padding: 0; box-sizing: border-box; }
  html, body { width: 1200px; height: 800px; overflow: hidden; }
  body { background: var(--backdrop); font-family: var(--body-font); position: relative; }

  .card {
    position: absolute;
    left: 302px;
    width: 595px;
    height: 340px;
    background: var(--white);
    overflow: hidden;
    box-shadow: 0 6px 18px rgba(0,0,0,0.18);
  }
  .card--back { top: 40px; }
  .card--front { top: 420px; }

  /* wordmark */
  .wordmark { position: absolute; display: flex; align-items: center; color: var(--navy); font-weight: 800; }
  .wordmark__dot { border-radius: 50%; background: var(--green); flex: none; }
  .wordmark__text { line-height: 1.05; text-transform: none; }
  .wordmark__name { display: block; }
  .wordmark__tag { display: block; }

  .card--back .wordmark { left: 50%; top: 50%; transform: translate(-50%, -50%); gap: 16px; }
  .card--back .wordmark__dot { width: 44px; height: 44px; }
  .card--back .wordmark__name { font-size: 44px; letter-spacing: 0.5px; }
  .card--back .wordmark__tag { font-size: 17.5px; }

  .card--front .wordmark { left: 386px; top: 88px; gap: 9px; }
  .card--front .wordmark__dot { width: 24px; height: 24px; }
  .card--front .wordmark__name { font-size: 26px; }
  .card--front .wordmark__tag { font-size: 10.5px; }

  /* front shapes */
  .front-shapes { position: absolute; inset: 0; }

  .contact { position: absolute; left: 38px; top: 44px; color: var(--white); }
  .contact__name { font-size: 21px; font-weight: 800; letter-spacing: 1px; text-transform: uppercase; margin-bottom: 12px; }
  .contact__name-last { color: var(--green); }
  .contact__address { font-size: 13px; line-height: 1.35; margin-bottom: 14px; }
  .contact__list { list-style: none; font-size: 13px; line-height: 1.45; }
  .contact__item { display: flex; align-items: center; gap: 9px; }
  .contact__icon { width: 11px; height: 11px; flex: none; fill: var(--green); }
  .contact__tagline { margin-top: 14px; font-size: 13px; line-height: 1.3; }
  .contact__tagline-accent { display: block; color: var(--green); }
</style>
</head>
<body>

  <section class="card card--back" aria-label="Card back">
    <div class="wordmark">
      <span class="wordmark__dot"></span>
      <span class="wordmark__text">
        <span class="wordmark__name">Corvella</span>
        <span class="wordmark__tag">Paintless Dent Removal</span>
      </span>
    </div>
  </section>

  <section class="card card--front" aria-label="Card front">
    <svg class="front-shapes" viewBox="0 0 595 340" width="595" height="340" aria-hidden="true">
      <path d="M0 0 H262 L338 200 H595 V340 H0 Z" fill="var(--navy)"/>
      <circle cx="600" cy="272" r="44" fill="var(--white)"/>
      <path d="M0 298 H468 L476 306 L468 316 H0 Z" fill="var(--green)"/>
      <rect x="396" y="226" width="132" height="8" fill="var(--white)"/>
      <rect x="408" y="262" width="120" height="8" fill="var(--white)"/>
      <rect x="420" y="298" width="108" height="8" fill="var(--white)"/>
      <circle cx="488" cy="213" r="9" fill="var(--white)"/>
      <circle cx="488" cy="249" r="9" fill="var(--white)"/>
      <circle cx="488" cy="285" r="9" fill="var(--white)"/>
    </svg>

    <div class="wordmark">
      <span class="wordmark__dot"></span>
      <span class="wordmark__text">
        <span class="wordmark__name">Corvella</span>
        <span class="wordmark__tag">Paintless Dent Removal</span>
      </span>
    </div>

    <div class="contact">
      <h1 class="contact__name">Dennis <span class="contact__name-last">Holbrook</span></h1>
      <p class="contact__address">PO Box 538 Ashmere<br>NY 11952</p>
      <ul class="contact__list">
        <li class="contact__item">
          <svg class="contact__icon" viewBox="0 0 12 12"><path d="M2.4 0.5 L4.4 2.8 L3.4 4.3 C4.1 5.8 6 7.7 7.6 8.5 L9.1 7.5 L11.5 9.5 L10.2 11.5 C5.5 11.2 0.7 6.4 0.5 1.8 Z"/></svg>
          631-472-8816
        </li>
        <li class="contact__item">
          <svg class="contact__icon" viewBox="0 0 12 12"><path d="M0.5 2 H11.5 V10 H0.5 Z M1.2 2.6 L6 6.4 L10.8 2.6" stroke="var(--navy)" stroke-width="0.9"/></svg>
          corvellapdr@mailnest.example
        </li>
        <li class="contact__item">
          <svg class="contact__icon" viewBox="0 0 12 12"><circle cx="6" cy="6" r="5.5"/><path d="M0.5 6 H11.5 M6 0.5 V11.5 M6 0.6 C3 3 3 9 6 11.4 M6 0.6 C9 3 9 9 6 11.4" stroke="var(--navy)" stroke-width="0.8" fill="none"/></svg>
          www.corvellapdr.example
        </li>
      </ul>
      <p class="contact__tagline">25 years of experience removing
        <span class="contact__tagline-accent">Dents, Dings and Hail Damage</span>
      </p>
    </div>
  </section>

</body>
</html>
```